Derek Osei Consulting

I've the wording, and the rough layout. See attached MicroSoft Word File. I need a professional to make my postcard "look pretty".

Industry/Entity Type

Consulting

```html
<!DOCTYPE html>
<html lang="en">
<head>
<meta charset="utf-8">
<title>Derek Osei Consulting – Postcard</title>
<link href="https://fonts.googleapis.com/css2?family=Archivo+Narrow:wght@400;700&family=Arimo:wght@700&display=swap" rel="stylesheet">
<style>
  :root {
    --card-blue: #2a80ac;
    --card-edge: #1f6a92;
    --figure-tone: #3b8db6;
    --ink-white: #ffffff;
    --ink-dark: #333333;
    --paper: #ffffff;
    --rule: #555555;
    --mailing-edge: #8a8a8a;
  }
  * { margin: 0; padding: 0; box-sizing: border-box; }
  html, body { width: 866px; height: 1200px; overflow: hidden; background: var(--paper); }
  .canvas { position: relative; width: 866px; height: 1200px; }

  .panel-blue { position: absolute; background: var(--card-blue); border: 1px solid var(--card-edge); color: var(--ink-white); }
  .front { left: 0; top: 0; width: 866px; height: 577px; }
  .back-message { left: 0; top: 622px; width: 466px; height: 578px; }
  .back-mailing { position: absolute; left: 466px; top: 622px; width: 400px; height: 578px; border: 1px solid var(--mailing-edge); background: var(--paper); }

  .headline {
    position: absolute; left: 33px;
    font-family: "Arimo", Arial, sans-serif; font-weight: 700;
    font-size: 24.5px; line-height: 29px; color: var(--ink-white);
  }
  .front .headline { top: 25px; }
  .back-message .headline { top: 49px; }

  .body-copy {
    position: absolute; font-family: "Archivo Narrow", "Arial Narrow", sans-serif;
    font-size: 13.2px; line-height: 15.7px; color: var(--ink-white);
  }
  .secret-list { list-style: none; }
  .front .secret-list { left: 29px; top: 257px; width: 472px; text-align: justify; }
  .back-message .secret-list { left: 29px; top: 165px; width: 418px; text-align: justify; }

  .pitch { left: 521px; top: 83px; width: 324px; text-align: justify; }
  .pitch p + p { margin-top: 15.7px; }

  .closing { left: 29px; top: 349px; width: 418px; text-align: justify; }
  .site-url {
    position: absolute; left: 29px; top: 485px;
    font-family: "Arimo", Arial, sans-serif; font-weight: 700; font-size: 14.5px; color: var(--ink-white);
  }

  .growth-chart { position: absolute; left: 0; top: 0; }
  .figure-placeholder { position: absolute; left: 326px; top: 52px; width: 108px; height: 148px; background: var(--figure-tone); border-radius: 6px; }

  .postage {
    position: absolute; left: 289px; top: 50px;
    font-family: "Arimo", Arial, sans-serif; font-weight: 700; font-size: 17.5px; line-height: 21px; color: var(--ink-dark);
  }
  .address-line { position: absolute; left: 62px; width: 284px; height: 1px; background: var(--rule); }
</style>
</head>
<body>
<div class="canvas">

  <section class="panel-blue front">
    <h1 class="headline">Learn Small Business Success<br>Secrets only “insiders”<br>know about:</h1>

    <svg class="growth-chart" width="866" height="577" viewBox="0 0 866 577" aria-hidden="true">
      <polyline points="227,257 279,227 301,240 323,204 422,193 450,139 470,150 502,108"
        fill="none" stroke="#ffffff" stroke-width="2"/>
      <polygon points="509,103 493,107 502,116" fill="#ffffff"/>
      <g fill="#ffffff">
        <circle cx="279" cy="227" r="4"/><circle cx="301" cy="240" r="4"/>
        <circle cx="323" cy="204" r="4"/><circle cx="422" cy="193" r="4"/>
        <circle cx="450" cy="139" r="4"/><circle cx="470" cy="150" r="4"/>
      </g>
    </svg>
    <div class="figure-placeholder" role="img" aria-label="Line drawing of a businessman with a briefcase climbing the growth chart"></div>

    <ol class="secret-list body-copy">
      <li>1.For those people who almost bought from you but did not, what’s the real reason why they didn’t buy from you? (And what to do about it?)</li>
      <li>2.How to turn an ordinary service that the customer can find everywhere, into something that the customer has to buy from you and only you?</li>
      <li>3.How to turn customer’s “scope creeping”, from a business loss, into a profit generator?</li>
      <li>4.What sort of person would be eager to sell to you at below fair market value?</li>
      <li>5.How to best utilize your limited operating capital?</li>
      <li>6.What sort of people would be a waste of time for your marketing effort?</li>
      <li>7.Other than money, how to motivate your employees?</li>
      <li>8.How to prevent your employees from stealing your business secrets? Setting up a competing business down the street from you? And worse still, taking your existing customers too?</li>
      <li>9.How to increase the perceived value of your products and services in the mind of your customers?</li>
      <li>10.How to market a commodity as a highly desired “must have” luxury item?</li>
      <li>11.How do you utilize a potentially bad situation and turn the situation into something positive? productive? and most importantly: Profitable???!!!</li>
    </ol>

    <div class="pitch body-copy">
      <p>“Insiders” who know the answers to these tricky business problems, get ahead in business and life. And the deeper their understanding to these tricky business problems, the more successful they become. They have very little stress from their businesses; they work very few hours by building their businesses into "auto pilot". They have more free time to enjoy life.</p>
      <p>If you don't know how to solve these tricky business problems, you will find yourself struggling with your businesses. You will find yourself working very long hours, and you have a lot of stress from running your business. If you are not even aware of the existence of this aspect of running a business, your business will not survive. You will become part of the statistic: 80% of businesses fail.</p>
      <p>What specific problems are slowing you down, or keeping you stuck, from reaching your ultimate goals? What specific challenges are causing you all the Stresses? Headaches? Frustrations?</p>
      <p>If your situation continues, how will it negatively impact you from achieving your personal fulfillment? If these problems and challenges could be solved, what are the benefits to you? Short term benefits? Long term benefits?</p>
      <p>To learn how to overcome these problems and challenges:</p>
    </div>
  </section>

  <section class="panel-blue back-message">
    <h2 class="headline">Learn Small Business Success<br>Secrets only “insiders”<br>know about:</h2>
    <ol class="secret-list body-copy">
      <li>1.How to make people want to have what you have for sale?</li>
      <li>2.How to turn new customers into repeat customers?</li>
      <li>3.How to make repeat customers comeback more often?</li>
      <li>4.How to spend less time with each customer, yet increase your profit on each business transaction?</li>
      <li>5.How to get more operating capital?</li>
      <li>6.How to buy low and sell high?</li>
      <li>7.How to manage employees and contractors?</li>
      <li>8.Which marketing methods are total waste of time and money?</li>
    </ol>
    <p class="closing body-copy">Why do 80% of all businesses fail??? Because their owners didn’t know what “business insiders” know. They worked very long hours, they had a lot of stresses and headaches, and in the end, due to their lack of business know-how, their businesses failed and they were left with a bunch of debt, a broken heart and sometimes a broken family too. Don’t become one of them! Become a real “insider”, run a successful business without stress and enjoy life! To find out more:</p>
    <div class="site-url">www.SmallFirmGrowthPlaybook.com</div>
  </section>

  <section class="back-mailing">
    <div class="postage">Postage<br>Paid</div>
    <div class="address-line" style="top:264px"></div>
    <div class="address-line" style="top:320px"></div>
    <div class="address-line" style="top:376px"></div>
    <div class="address-line" style="top:431px"></div>
  </section>

</div>
</body>
</html>
```